Business cards

Design business cards for our company. Just a straight, business like design with the logo, name, function and contact details

Target Market(s)

We are a innovative technological company active in water treatment

Industry/Entity Type

Water management

Contact Information for Business Card

Name, Function, email, telephone number, link to website

```html
<!DOCTYPE html>
<html lang="en">
<head>
<meta charset="utf-8">
<title>Aquore – Business Cards</title>
<link rel="stylesheet" href="https://fonts.googleapis.com/css2?family=Open+Sans:wght@400;600;700&display=swap">
<style>
  :root {
    --bg: #e4e5e7;
    --card-white: #ffffff;
    --brand-blue: #2f9bd6;
    --brand-grey: #9a9896;
    --pattern-light: #a9a6a3;
    --pattern-dark: #8d8a87;
    --ink: #1f1f1f;
    --rule: #3a3a3a;
  }
  * { box-sizing: border-box; margin: 0; padding: 0; }
  html, body { width: 1200px; height: 780px; overflow: hidden; }
  body {
    background: var(--bg);
    font-family: "Open Sans", Arial, sans-serif;
    display: flex;
    align-items: center;
    justify-content: center;
    gap: 50px;
  }
  .card {
    width: 540px;
    height: 309px;
    position: relative;
    box-shadow: 0 10px 24px rgba(0,0,0,0.18);
    overflow: hidden;
  }
  /* Front */
  .card-front { background: var(--card-white); }
  .brand {
    position: absolute;
    left: 48px;
    top: 118px;
    display: flex;
    align-items: center;
    gap: 10px;
  }
  .brand-name {
    font-size: 40px;
    font-weight: 600;
    color: var(--brand-blue);
    letter-spacing: 0.5px;
  }
  .brand-dot {
    width: 30px; height: 30px;
    border-radius: 50%;
    background: var(--brand-blue);
  }
  .divider {
    position: absolute;
    left: 272px;
    top: 48px;
    width: 1px;
    height: 150px;
    background: var(--rule);
  }
  .person {
    position: absolute;
    left: 296px;
    top: 44px;
  }
  .person-name {
    font-size: 25px;
    font-weight: 700;
    color: var(--brand-blue);
    line-height: 1.1;
  }
  .person-role {
    font-size: 13px;
    font-weight: 600;
    color: var(--ink);
    margin-top: 2px;
  }
  .contact-list { list-style: none; margin-top: 16px; }
  .contact-item {
    display: flex;
    align-items: center;
    gap: 8px;
    font-size: 13px;
    color: var(--ink);
    line-height: 20px;
  }
  .contact-icon { width: 13px; height: 13px; flex: none; }
  .address-band {
    position: absolute;
    left: 0;
    bottom: 24px;
    width: 100%;
    height: 30px;
    display: flex;
  }
  .address-text {
    flex: 1;
    background: var(--brand-blue);
    color: #fff;
    font-size: 14px;
    line-height: 30px;
    padding-left: 40px;
  }
  .address-accent {
    width: 70px;
    background: var(--brand-grey);
  }
  /* Back */
  .card-back {
    background: linear-gradient(135deg, var(--pattern-light), var(--pattern-dark));
  }
  .back-pattern {
    position: absolute;
    inset: 0;
    background: linear-gradient(160deg, #b1aeab 0%, #9b9895 55%, #8e8b88 100%);
  }
  .back-brand {
    position: absolute;
    right: 40px;
    top: 130px;
    display: flex;
    align-items: center;
    gap: 8px;
  }
  .back-brand .brand-name { color: #fff; font-size: 30px; }
  .back-brand .brand-dot { background: #fff; width: 22px; height: 22px; }
</style>
</head>
<body>
  <section class="card card-front" aria-label="Business card front">
    <div class="brand">
      <span class="brand-name">Aquore</span>
      <span class="brand-dot"></span>
    </div>
    <div class="divider"></div>
    <div class="person">
      <p class="person-name">Mila Hartwell</p>
      <p class="person-role">Managing Director</p>
      <ul class="contact-list">
        <li class="contact-item">
          <svg class="contact-icon" viewBox="0 0 16 16"><path fill="#2f9bd6" d="M3.5 1.5l2.5 0 1 3.5-1.6 1.2a8 8 0 0 0 4.4 4.4l1.2-1.6 3.5 1v2.5c0 .8-.7 1.5-1.5 1.5C6.5 14 2 9.5 2 3c0-.8.7-1.5 1.5-1.5z"/></svg>
          (555) 014-2238
        </li>
        <li class="contact-item">
          <svg class="contact-icon" viewBox="0 0 16 16"><rect x="1" y="3" width="14" height="10" rx="1.5" fill="#2f9bd6"/><path d="M1.5 4l6.5 5 6.5-5" stroke="#fff" stroke-width="1.3" fill="none"/></svg>
          hello@aquore.com
        </li>
        <li class="contact-item">
          <svg class="contact-icon" viewBox="0 0 16 16"><circle cx="8" cy="8" r="7" fill="#2f9bd6"/><path d="M1 8h14M8 1c-3 3.5-3 10.5 0 14M8 1c3 3.5 3 10.5 0 14" stroke="#fff" stroke-width="1" fill="none"/></svg>
          www.aquore.com
        </li>
      </ul>
    </div>
    <div class="address-band">
      <p class="address-text">480 Lakeside Ave. Suite 12 Riverton, TX 75001</p>
      <span class="address-accent"></span>
    </div>
  </section>

  <section class="card card-back" aria-label="Business card back">
    <div class="back-pattern" role="img" aria-label="Repeating pattern of the company symbol in grey, silver and black tones"></div>
    <div class="back-brand">
      <span class="brand-name">Aquore</span>
      <span class="brand-dot"></span>
    </div>
  </section>
</body>
</html>
```